Stationary (letterhead, envelopes, business cards and e-mail signature) for law firm
Law Office of Warren T. Felding
Creative Brief
Professional
Warren T. Felding
Attorney at Law
41 Linden Court, Suite 500 Carrow Falls, Nevada 92731
wfelding@lawwtf-example.com
www.lawwtf-example.com
I would also like my direct dial phone number to appear on the card (in addition to my main number. The Direct number is (714) 555-0187
I would like my logo and maybe my website address to appear on the back. Please be creative.

```html
<!DOCTYPE html>
<html lang="en">
<head>
<meta charset="utf-8">
<title>Law Office of Warren T. Felding – Stationery</title>
<link href="https://fonts.googleapis.com/css2?family=Cinzel:wght@400;600&display=swap" rel="stylesheet">
<style>
  :root{
    --navy:#1b1f4d;
    --navy-soft:#2b3068;
    --paper:#ffffff;
    --stage:#d3d3d3;
    --card-grey:#8d8d8d;
    --ink:#2a2d55;
    --light-text:#e8e9f2;
    --rule:#9a9cb5;
  }
  *{margin:0;padding:0;box-sizing:border-box}
  html,body{width:1200px;height:754px;overflow:hidden;background:var(--stage)}
  body{position:relative;font-family:'Cinzel',serif}
  .piece{position:absolute;background:var(--paper);overflow:hidden;box-shadow:0 1px 3px rgba(0,0,0,.25)}
  .wave{position:absolute;left:0;width:100%}
  .brand{font-family:'Cinzel',serif;font-weight:600;color:var(--navy);letter-spacing:.02em;white-space:nowrap}
  .firm{color:var(--ink);line-height:1.15;white-space:nowrap}
  .firm small{display:block;font-size:.55em;letter-spacing:.25em;color:#6a6d8c}
  .light{color:var(--light-text)}

  .letterhead{left:48px;top:34px;width:509px;height:669px}
  .letterhead .head{position:absolute;left:26px;top:38px;display:flex;align-items:center;gap:10px}
  .letterhead .brand{font-size:24px}
  .letterhead .firm{font-size:17px;border-left:1px solid var(--rule);padding-left:10px}
  .letterhead .foot{position:absolute;left:24px;bottom:20px;font-size:9.5px;line-height:1.55;white-space:nowrap}

  .card-front{left:588px;top:48px;width:204px;height:120px}
  .card-front .head{position:absolute;left:8px;top:8px;display:flex;align-items:center;gap:5px}
  .card-front .brand{font-size:11px}
  .card-front .firm{font-size:8px;border-left:1px solid var(--rule);padding-left:5px}
  .card-front .person{position:absolute;right:10px;top:44px;text-align:right;font-size:7.5px;color:var(--ink);line-height:1.3}
  .card-front .person span{display:block;font-size:5px;letter-spacing:.1em}
  .card-front .contact{position:absolute;left:8px;bottom:7px;font-size:5px;line-height:1.45;white-space:nowrap}

  .card-back{display:flex;flex-direction:column;align-items:center;justify-content:center;gap:18px;border-radius:4px}
  .card-back .brand{font-size:24px}
  .card-back .web{font-size:6px;letter-spacing:.1em}
  .card-navy{left:667px;top:192px;width:202px;height:120px;background:var(--navy)}
  .card-navy .brand,.card-grey .brand{color:var(--paper)}
  .card-white{left:888px;top:96px;width:206px;height:120px;border:1px solid #c5c5c5}
  .card-white .web{color:var(--ink)}
  .card-grey{left:905px;top:240px;width:206px;height:120px;background:var(--card-grey)}

  .envelope{left:576px;top:377px;width:557px;height:326px}
  .envelope .flap-mark{position:absolute;left:0;top:14px;width:100%;text-align:center;transform:rotate(180deg);font-size:32px;color:var(--paper)}
  .envelope .head{position:absolute;left:14px;top:115px;display:flex;align-items:center;gap:8px}
  .envelope .brand{font-size:17px}
  .envelope .firm{font-size:12.5px;border-left:1px solid var(--rule);padding-left:8px}
  .envelope .foot{position:absolute;left:14px;bottom:22px;font-size:9px;line-height:1.5;white-space:nowrap}
</style>
</head>
<body>

<section class="piece letterhead">
  <div class="head">
    <span class="brand">Felding</span>
    <div class="firm"><small>Law Office of</small>Warren T. Felding</div>
  </div>
  <svg class="wave" style="bottom:0;height:115px" viewBox="0 0 509 115" preserveAspectRatio="none">
    <path d="M0 40 C120 0 260 10 360 28 C430 40 480 34 509 22 L509 115 L0 115Z" fill="var(--navy)"/>
    <path d="M0 46 C130 8 260 18 360 34 C430 46 480 40 509 28" fill="none" stroke="var(--navy-soft)" stroke-width="2"/>
  </svg>
  <div class="foot light">41 Linden Court, Suite 500, Carrow Falls, Nevada 92731<br>Phone (714) 555-0187 | Fax (702) 555-0142<br>Email wfelding@lawwtf-example.com | www.lawwtf-example.com</div>
</section>

<section class="piece card-front">
  <div class="head">
    <span class="brand">Felding</span>
    <div class="firm"><small>Law Office of</small>Warren T. Felding</div>
  </div>
  <div class="person">Warren T. Felding<span>Attorney at Law</span></div>
  <svg class="wave" style="bottom:0;height:50px" viewBox="0 0 204 50" preserveAspectRatio="none">
    <path d="M0 12 C60 0 120 4 204 20 L204 50 L0 50Z" fill="var(--navy)"/>
  </svg>
  <div class="contact light">41 Linden Court, Suite 500, Carrow Falls, NV 92731<br>Direct (714) 555-0187 | Main (702) 555-0142<br>wfelding@lawwtf-example.com</div>
</section>

<section class="piece card-back card-navy">
  <span class="brand">Felding</span>
  <span class="web light">www.lawwtf-example.com</span>
</section>

<section class="piece card-back card-white">
  <span class="brand">Felding</span>
  <span class="web">www.lawwtf-example.com</span>
</section>

<section class="piece card-back card-grey">
  <span class="brand">Felding</span>
  <span class="web light">www.lawwtf-example.com</span>
</section>

<section class="piece envelope">
  <svg class="wave" style="top:0;height:96px" viewBox="0 0 557 96" preserveAspectRatio="none">
    <path d="M0 0 L557 0 L557 78 C470 92 360 96 278 88 C180 80 80 74 0 84Z" fill="var(--navy)"/>
  </svg>
  <div class="flap-mark brand">Felding</div>
  <div class="head">
    <span class="brand">Felding</span>
    <div class="firm"><small>Law Office of</small>Warren T. Felding</div>
  </div>
  <svg class="wave" style="bottom:0;height:80px" viewBox="0 0 557 80" preserveAspectRatio="none">
    <path d="M0 28 C150 0 300 8 400 22 C470 32 520 26 557 14 L557 80 L0 80Z" fill="var(--navy)"/>
    <path d="M0 34 C150 6 300 14 400 28 C470 38 520 32 557 20" fill="none" stroke="var(--navy-soft)" stroke-width="2"/>
  </svg>
  <div class="foot light">41 Linden Court, Suite 500<br>Carrow Falls, Nevada 92731</div>
</section>

</body>
</html>
```